Industrial Professional Business Card Design (Vantrel KX)

Would like professional looking business cards. Not too busy leaning towards minimal. Should have a slogan like:
"Industrial Automation and Control".

We are a tech company that programs industrial PLC computers. We also develop custom hardware solutions. Please use the logo for inspiration.

Target Market(s)

Mining, industrial, processing, automation, factory

Industry/Entity Type

Engineering

Contact Information for Business Card

Name, phone, email, website. job title.

Font styles to use
Other font styles liked:
• droid sans

Requirements
Must have
• Use colours that go well with the logo. Not too busy design.

```html
<!DOCTYPE html>
<html lang="en">
<head>
<meta charset="utf-8">
<title>Vantrel KX — Business Card</title>
<link rel="stylesheet" href="https://fonts.googleapis.com/css2?family=Michroma&family=Noto+Sans:wght@400;700&display=swap">
<style>
  :root {
    --stage: #2c2c2c;
    --navy: #1b3a6b;
    --blue-deep: #1d3563;
    --blue-mid: #1f5f8e;
    --orange: #f26a21;
    --ink: #2f2f35;
    --rule: #d6d8dc;
    --paper: #ffffff;
  }
  * { margin: 0; padding: 0; box-sizing: border-box; }
  html, body { width: 1200px; height: 866px; overflow: hidden; }
  body {
    background: var(--stage);
    display: flex;
    align-items: center;
    justify-content: center;
    gap: 40px;
    font-family: "Noto Sans", sans-serif;
  }
  .card {
    width: 540px;
    height: 309px;
    position: relative;
    overflow: hidden;
    box-shadow: 0 14px 30px rgba(0,0,0,0.45);
  }
  /* Front: contact side */
  .card--front { background: var(--paper); }
  .contact { position: absolute; left: 36px; top: 38px; }
  .contact__name {
    font-family: "Michroma", sans-serif;
    font-size: 15px;
    letter-spacing: 0.5px;
    color: var(--navy);
  }
  .contact__name .surname { color: var(--orange); }
  .contact__title { font-size: 13px; color: var(--ink); margin-top: 2px; }
  .contact__line {
    display: flex; align-items: center; gap: 8px;
    font-size: 12.5px; color: var(--ink); margin-top: 6px;
  }
  .contact__line:first-of-type { margin-top: 12px; }
  .contact__line svg { width: 15px; height: 15px; flex: none; }
  .wordmark {
    display: flex; align-items: center; gap: 12px;
    font-family: "Noto Sans", sans-serif;
    font-weight: 400;
  }
  .wordmark__dot { border-radius: 50%; flex: none; }
  .card--front .wordmark { position: absolute; right: 44px; top: 138px; }
  .card--front .wordmark__text { font-size: 40px; color: var(--navy); letter-spacing: 0.5px; }
  .card--front .wordmark__dot { width: 26px; height: 26px; background: var(--orange); }
  .divider { position: absolute; left: 150px; right: 36px; top: 236px; height: 1px; background: var(--rule); }
  .website {
    position: absolute; right: 40px; top: 250px;
    font-size: 14px; color: var(--navy); letter-spacing: 0.5px;
  }
  .website .domain { color: var(--orange); }
  /* Back: brand side */
  .card--back {
    background:
      radial-gradient(circle at 60% 40%, rgba(40,120,170,0.55) 0%, rgba(40,120,170,0) 60%),
      linear-gradient(135deg, var(--blue-mid) 0%, var(--blue-deep) 100%);
    display: flex; flex-direction: column; align-items: center; justify-content: center;
  }
  .card--back .wordmark__text { font-size: 46px; color: var(--paper); letter-spacing: 0.5px; }
  .card--back .wordmark__dot { width: 28px; height: 28px; background: var(--orange); }
  .slogan {
    margin-top: 18px;
    font-family: "Michroma", sans-serif;
    font-size: 12.5px;
    letter-spacing: 1px;
    text-transform: uppercase;
    color: var(--orange);
  }
</style>
</head>
<body>
  <section class="card card--front">
    <div class="contact">
      <p class="contact__name">MARCUS <span class="surname">HALE</span></p>
      <p class="contact__title">Managing Director</p>
      <p class="contact__line">
        <svg viewBox="0 0 16 16" aria-hidden="true"><rect x="1" y="1" width="14" height="14" rx="3" fill="none" stroke="#1b3a6b" stroke-width="1.4"/><path d="M5.5 4.5c-.8.6-1 1.8-.2 3.2s2 2.7 3.4 3.4c1 .4 1.8.3 2.3-.3l-1.3-1.3-1 .5c-.8-.4-1.6-1.2-2-2l.5-1z" fill="#1b3a6b"/></svg>
        044-987 650 312
      </p>
      <p class="contact__line">
        <svg viewBox="0 0 16 16" aria-hidden="true"><rect x="1" y="3" width="14" height="10" fill="#1b3a6b"/><path d="M1 3l7 6 7-6" fill="none" stroke="#fff" stroke-width="1.2"/></svg>
        info@vantrelkx.com
      </p>
    </div>
    <div class="wordmark">
      <span class="wordmark__dot"></span>
      <span class="wordmark__text">Vantrel KX</span>
    </div>
    <div class="divider"></div>
    <p class="website">www.<span class="domain">vantrelkx</span>.com</p>
  </section>

  <section class="card card--back">
    <div class="wordmark">
      <span class="wordmark__dot"></span>
      <span class="wordmark__text">Vantrel KX</span>
    </div>
    <p class="slogan">Industrial Automation and Control</p>
  </section>
</body>
</html>
```